Inclusive life skills courses upskilling in wellbeing, academic success and career readines

I need a web design that is corporate and engaging. It needs to capture what we do and our core course offering. We develop courses and make customised course provision that cultivate 21st-century competencies that support academic achievement and social and emotional skills fostering personal growth and academic skill development that are relevant and timely for the learner. This prepares them for present and future challenges and opportunities, while contributing to students’ career portfolio with an accredited, relevant and adaptive provision. Our initial course is a Level 1 course. Here are the tentative course details. The courses will be accessed through the site, it should be crisp, clear and simple.

Level 1 Skills for Life & Work is part of the TRVC designed to equip students with essential life skills. Accredited and focused on social-emotional learning, academic skills, and work preparation, this program offers a comprehensive approach to student development.

Course Structure
Certificates: Six short courses (micro learning) each can be taken individually or as a whole offering.
Credit Integration: Completing all six courses cumulates credits.
Course Duration: Each course involves 3 hours of content, 6 hours of practical application, and 3 hours of portfolio work and reflection.
*Note HEMB Tariff is possible with PKR L3. An accredited CPD course may be simpler.
Short Courses within Level 1 TRVC
Self-Awareness: A sense of purpose. understand emotions, thoughts, and values and how they influence behavior across contexts. This includes capacities to recognize one’s strengths and limitations with a well- grounded sense of confidence and purpose.
Self-Management: A sense of self. Manage emotions, and behaviors in different situations to achieve goals and aspirations while managing time, stress and balance.
Building Resilience: Overcome challenges and adversity. Develop the confidence to face life’s challenges and reach your full potential, feeling more capable and in control of your life
Motivation & Mindset: Cultivating a positive approach and drive. This requires effective study skills, a growth mindset, gratitude and techniques to find work life balance.
Communication: Build rapport. Approach different types of conversation with confidence and clarity, listen and relate to others and manage requests.
Making an Impact: Develop assertiveness and confidence. Confidently share your ideas and opinions, improve your influencing skills and explore the trust equation.
Skills badges in progress: problem-solving, leadership, teamwork, listening, aiming high, staying positive.
Approach
Student-Centric: Courses blend digital learning with practical application.
Flexibility: Self-paced, adaptable to independent or classroom learning.
Digital Integration: Includes digital portfolio of practice (DPP) and skill bite certificates.
Practical Application: Emphasizes real-world skills and portfolio building.
Progress monitoring: Students are empowered in their learning and development.
Customization: AI-driven to tailor courses to student needs.
Aim and Impact
This qualification is designed to be directly relevant and applicable to students’ daily lives, encouraging personal growth and skill development. It’s a flexible offering, which is self-paced or blended (flipped) with the practical components integrated into classes. Teachers and students experience flipped learning and then practice and develop portfolio through subject teaching.

Progression Levels (PKR or CPD)

Level 1 Training for Life and Work (CPD Credits)
Level 2 Project Management and Teamwork (CPD Credits)
Level 3 Leading, Mentoring, Coaching
Level 4 Innovative Entrepreneurship

Please note: A logo will be available. The colour branding is similar to this:https://lessonvane.example/ and this: https://tutorbrisk.example/

Industry/Entity Type

Education (K-12, university and corporate)

Number of Pages Required

1 page

Font styles to use
Serif

Colors
0054AA
0677BA
7BADD7
CADEEF
E8F1F8
0094D4
00A9DD
6FCCEA
C7EBF8
E9F6FB
00AB8E
00BBA5
67D7C9
C6EFE9
E9F9F6

Requirements
Nice to have
• Simple, captures what we do.

```html
<!DOCTYPE html>
<html lang="en">
<head>
<meta charset="utf-8">
<title>Inclusive Life Skills Courses</title>
<link href="https://fonts.googleapis.com/css2?family=Tinos:wght@400;700&family=Montserrat:wght@400;500;600&display=swap" rel="stylesheet">
<style>
:root{
  --teal:#00AB8E;
  --teal-2:#00BBA5;
  --teal-3:#67D7C9;
  --blue:#0094D4;
  --blue-2:#00A9DD;
  --navy:#0c2f40;
  --navy-2:#12465d;
  --ink:#111c24;
  --soft:#f1f4f7;
  --line:#dfe6ec;
  --white:#ffffff;
}
*{box-sizing:border-box;margin:0;padding:0}
html,body{width:1200px;height:3606px;overflow:hidden}
body{position:relative;font-family:"Montserrat",Arial,sans-serif;color:var(--ink);background:var(--white)}
.serif{font-family:"Tinos","Times New Roman",serif}
.abs{position:absolute}
.btn{position:absolute;display:flex;align-items:center;justify-content:center;gap:6px;font-family:"Montserrat",sans-serif;font-weight:600;font-size:14px;color:var(--white);height:43px}
.btn-solid{background:var(--blue)}
.btn-ghost{border:1.5px solid var(--white)}
.btn svg{width:13px;height:13px}

/* header */
.site-header{position:absolute;left:0;top:0;width:1200px;height:100px;background:var(--white)}
.logo{font-family:"Tinos",serif;font-weight:700;font-size:22px;color:var(--teal)}
.main-nav{position:absolute;left:406px;top:40px;display:flex;gap:25px;font-size:14px;color:#222}
.main-nav .active{color:var(--teal);font-weight:600}

/* hero */
.hero{position:absolute;left:0;top:100px;width:1200px;height:575px}
.hero-photo{position:absolute;inset:0;background:linear-gradient(180deg,#8a8f8a 0%,#5f6f70 35%,#1f4a5b 62%,#0f3a4d 100%)}
.hero-arrow{position:absolute;top:270px;width:37px;height:37px;background:var(--teal-2);display:flex;align-items:center;justify-content:center}
.hero h1{position:absolute;left:0;width:1200px;top:280px;text-align:center;font-size:38px;color:var(--white)}
.hero h2{position:absolute;left:0;width:1200px;top:325px;text-align:center;font-size:30px;font-weight:400;color:var(--teal-3)}
.hero p{position:absolute;left:300px;width:600px;top:380px;text-align:center;font-size:14.5px;line-height:19px;color:var(--white)}

/* courses */
.courses{position:absolute;left:0;top:675px;width:1200px;height:520px;background:var(--soft);overflow:hidden}
.eyebrow{position:absolute;left:0;width:1200px;text-align:center;font-family:"Tinos",serif;font-weight:700;font-size:17px;color:var(--teal)}
.eyebrow span::before,.eyebrow span::after{content:"";display:inline-block;width:55px;height:1.5px;background:var(--teal);vertical-align:middle;margin:0 8px}
.section-title{position:absolute;left:0;width:1200px;text-align:center;font-family:"Tinos",serif;font-weight:700;font-size:34px;color:var(--teal)}
.course-card{position:absolute;top:155px;width:248px;background:var(--white);border-radius:6px;text-align:center;box-shadow:0 2px 8px rgba(0,0,0,.05)}
.course-card.current{border:2px solid var(--blue-2)}
.course-img{margin:11px auto 0;width:224px;height:171px;border-radius:4px}
.course-card .lvl{font-family:"Tinos",serif;font-weight:700;font-size:15px;color:var(--teal);margin-top:14px}
.course-card .name{font-family:"Tinos",serif;font-size:15px;line-height:18px;color:var(--ink);padding:0 14px 18px}
.course-card .name b{font-weight:700}

/* level 1 */
.level{position:absolute;left:0;top:1195px;width:1200px;height:900px}
.level .lvl-label{position:absolute;left:0;width:1200px;top:50px;text-align:center;font-family:"Tinos",serif;font-weight:700;font-size:31px;color:var(--teal)}
.level h3{position:absolute;left:0;width:1200px;top:85px;text-align:center;font-family:"Tinos",serif;font-size:33px;font-weight:400;color:var(--ink)}
.level h3 b{font-weight:700}
.level .intro{position:absolute;left:310px;width:580px;top:130px;text-align:center;font-size:14.5px;line-height:19px}
.tab{position:absolute;top:240px;height:43px;border:1.5px solid var(--blue-2);display:flex;align-items:center;justify-content:center;font-size:14px;color:var(--blue)}
.tab.on{background:#e9f6fb}
.feature{position:absolute;width:291px;height:217px;background:var(--white);box-shadow:0 3px 12px rgba(0,40,70,.08);text-align:center}
.feature svg{display:block;margin:38px auto 0;width:70px;height:70px}
.feature h4{font-family:"Tinos",serif;font-weight:700;font-size:19px;color:var(--teal);margin-top:18px}
.feature p{font-size:14px;line-height:19px;margin-top:2px;padding:0 20px}

/* invest */
.invest{position:absolute;left:0;top:2095px;width:1200px;height:408px;background:linear-gradient(90deg,#0f3a4d 0%,#1a4d62 55%,#143f52 100%)}
.invest h3{position:absolute;left:126px;top:75px;font-family:"Tinos",serif;font-weight:700;font-size:33px;color:var(--teal-2)}
.invest p{position:absolute;left:126px;top:120px;width:470px;font-size:14.3px;line-height:18.8px;color:var(--white)}
.invest-photo{position:absolute;left:802px;top:60px;width:272px;height:348px;border-radius:136px 136px 0 0;background:linear-gradient(180deg,#18c2ae,#0aa08f)}
.invest-ring{position:absolute;left:815px;top:60px;width:58px;height:58px;border:10px solid var(--blue-2);border-radius:50%}

/* testimonials */
.testimonials{position:absolute;left:0;top:2503px;width:1200px;height:540px}
.quote-mark{position:absolute;left:0;width:1200px;top:140px;text-align:center;font-family:"Tinos",serif;font-weight:700;font-size:70px;line-height:60px;color:#d4dde3}
.testimonials h4{position:absolute;left:0;width:1200px;top:198px;text-align:center;font-family:"Tinos",serif;font-weight:700;font-size:21px}
.testimonials .quote{position:absolute;left:320px;width:560px;top:225px;text-align:center;font-size:14.2px;line-height:18.8px}
.t-arrow{position:absolute;top:237px;width:37px;height:37px;background:var(--teal-2);display:flex;align-items:center;justify-content:center}
.avatar{position:absolute;left:560px;top:314px;width:78px;height:78px;border-radius:50%;border:2px solid var(--teal-2);background:linear-gradient(135deg,#f4e6c8,#e2b46a)}
.t-name{position:absolute;left:0;width:1200px;top:398px;text-align:center;font-family:"Tinos",serif;font-weight:700;font-size:15px}
.t-role{position:absolute;left:0;width:1200px;top:416px;text-align:center;font-size:14px}
.dots{position:absolute;left:563px;top:461px;display:flex;gap:5px}
.dots i{width:10px;height:10px;border-radius:50%;background:#c6efe9}
.dots i.on{background:var(--teal)}

/* footer */
.site-footer{position:absolute;left:0;top:3125px;width:1200px;height:481px;background:var(--navy)}
.partners{position:absolute;left:63px;top:3040px;width:1077px;height:163px;border-radius:8px;background:linear-gradient(90deg,#0aa0dc 0%,#0aa8c8 50%,#14bca4 100%)}
.partners h3{position:absolute;left:63px;top:68px;font-family:"Tinos",serif;font-weight:700;font-size:31px;color:var(--white)}
.badge{position:absolute;top:27px;width:112px;height:112px;border-radius:50%;background:var(--white)}
.badge i{position:absolute;left:28px;top:28px;width:56px;height:56px;border-radius:50%;background:#e1e7ec}
.f-col h5{font-family:"Tinos",serif;font-weight:700;font-size:17px;color:var(--white)}
.f-links{list-style:none;margin-top:14px}
.f-links li{font-size:14px;color:#c9d6dd;height:31px}
.f-contact{list-style:none;margin-top:14px}
.f-contact li{display:flex;gap:12px;font-size:14px;line-height:18px;color:#c9d6dd;margin-bottom:16px}
.f-contact svg{width:12px;height:12px;flex:none;margin-top:3px}
.news p{font-size:14px;line-height:19px;color:#c9d6dd;margin-top:14px;width:330px}
.news .field{margin-top:22px;width:323px;height:37px;border:1px solid #8fa5b1;display:flex;align-items:center;gap:8px;padding-left:12px;font-size:14px;color:#c9d6dd}
.news .sub{margin-top:15px;width:323px;height:37px;background:var(--blue);display:flex;align-items:center;justify-content:center;gap:6px;font-weight:600;font-size:14px;color:var(--white)}
.f-bottom{position:absolute;left:63px;top:416px;width:1075px;border-top:1px solid #2a4b5b}
.copyright{position:absolute;left:63px;top:442px;font-size:13px;color:#c9d6dd}
.social{position:absolute;top:440px;width:22px;height:22px;background:#8fa5b1}
</style>
</head>
<body>

<header class="site-header">
  <div class="logo abs" style="left:63px;top:36px">Logo Here</div>
  <nav class="main-nav">
    <span class="active">Home</span><span>About ⌄</span><span>Our Courses ⌄</span><span>FAQs</span><span>Resources</span><span>Contact Us</span>
  </nav>
  <a class="btn btn-solid" style="left:977px;top:28px;width:160px">Enroll Today <svg viewBox="0 0 14 14"><path d="M1 7h11M8 3l4 4-4 4" stroke="#fff" stroke-width="1.6" fill="none"/></svg></a>
</header>

<section class="hero">
  <div class="hero-photo" role="img" aria-label="Smiling group of diverse students holding books in a classroom"></div>
  <div class="hero-arrow" style="left:0"><svg width="16" height="16" viewBox="0 0 14 14"><path d="M13 7H2M6 3L2 7l4 4" stroke="#fff" stroke-width="1.6" fill="none"/></svg></div>
  <div class="hero-arrow" style="left:1163px"><svg width="16" height="16" viewBox="0 0 14 14"><path d="M1 7h11M8 3l4 4-4 4" stroke="#fff" stroke-width="1.6" fill="none"/></svg></div>
  <h1 class="serif">Inclusive Life Skills Courses</h1>
  <h2 class="serif">Upskilling in Wellbeing</h2>
  <p>Through focused learning and practical techniques, our courses can help you navigate life's challenges more effectively, leading to happier, healthier lives.</p>
  <a class="btn btn-solid" style="left:429px;top:457px;width:160px">Enroll Today <svg viewBox="0 0 14 14"><path d="M1 7h11M8 3l4 4-4 4" stroke="#fff" stroke-width="1.6" fill="none"/></svg></a>
  <a class="btn btn-ghost" style="left:611px;top:457px;width:160px">Our Courses <svg viewBox="0 0 14 14"><path d="M1 7h11M8 3l4 4-4 4" stroke="#fff" stroke-width="1.6" fill="none"/></svg></a>
</section>

<section class="courses">
  <div class="abs" style="left:1045px;top:375px;width:260px;height:260px;border:55px solid #e3e7ea;border-radius:50%"></div>
  <div class="eyebrow" style="top:66px"><span>Our Courses</span></div>
  <h2 class="section-title" style="top:86px">Progression Levels (PKR or CPD)</h2>

  <div class="course-card current" style="left:63px">
    <div class="course-img" role="img" aria-label="Wooden letter tiles spelling life, work and balance on a desk" style="background:linear-gradient(135deg,#c89a72,#9d6f4c)"></div>
    <div class="lvl">Level 1</div>
    <div class="name"><b>Training for Life and Work</b><br>(CPD Credits)</div>
  </div>
  <div class="course-card" style="left:338px">
    <div class="course-img" role="img" aria-label="Hand-drawn project management diagram with coloured pencils" style="background:linear-gradient(135deg,#eef0e6,#c9d9b8)"></div>
    <div class="lvl">Level 2</div>
    <div class="name"><b>Project Management<br>and Teamwork</b><br>(CPD Credits)</div>
  </div>
  <div class="course-card" style="left:613px">
    <div class="course-img" role="img" aria-label="Team of business professionals standing together" style="background:linear-gradient(135deg,#9aa6b0,#3d4a57)"></div>
    <div class="lvl">Level 3</div>
    <div class="name"><b>Leading, Mentoring,<br>Coaching</b></div>
  </div>
  <div class="course-card" style="left:889px">
    <div class="course-img" role="img" aria-label="Chalkboard with entrepreneur concept words" style="background:linear-gradient(135deg,#2b2f33,#14171a)"></div>
    <div class="lvl">Level 4</div>
    <div class="name"><b>Innovative Entrepreneurship</b></div>
  </div>
</section>

<section class="level">
  <div class="lvl-label">Level 1</div>
  <h3><b>Training for Life and Work</b> (CPD Credits)</h3>
  <p class="intro">Level 1 Skills for Life &amp; Work is part of the TRVC designed to equip students with essential life skills. Accredited and focused on social-emotional learning, academic skills, and work preparation this program offers a comprehensive approach to student development.</p>
  <div class="tab" style="left:302px;width:159px">Course Structure</div>
  <div class="tab" style="left:482px;width:138px">Short Courses</div>
  <div class="tab on" style="left:641px;width:105px">Approach</div>
  <div class="tab" style="left:766px;width:131px">Aim &amp; Impact</div>

  <div class="feature" style="left:126px;top:338px">
    <svg viewBox="0 0 70 70" fill="none" stroke="#00A9DD" stroke-width="2.2"><circle cx="32" cy="18" r="11"/><path d="M12 64V50c0-8 8-13 20-13s20 5 20 13v14"/><path d="M26 38l6 10 6-10"/><rect x="42" y="50" width="18" height="5"/><rect x="44" y="55" width="18" height="5"/></svg>
    <h4>Student-Centric</h4><p>Courses blend digital learning<br>with practical application.</p>
  </div>
  <div class="feature" style="left:453px;top:338px">
    <svg viewBox="0 0 70 70" fill="none" stroke="#00A9DD" stroke-width="2.2"><path d="M6 20v40h58V20"/><path d="M10 16v40c9-2 18-1 25 4 7-5 16-6 25-4V24"/><path d="M35 20v40"/><circle cx="52" cy="16" r="11"/><path d="M52 10v6l4 3"/></svg>
    <h4>Flexibility</h4><p>Self-paced, adaptable to<br>independent or classroom learning.</p>
  </div>
  <div class="feature" style="left:780px;top:338px">
    <svg viewBox="0 0 70 70" fill="none" stroke="#00A9DD" stroke-width="2.2"><circle cx="28" cy="35" r="22"/><ellipse cx="28" cy="35" rx="10" ry="22"/><path d="M6 35h44M10 24h36M10 46h36"/><rect x="52" y="14" width="7" height="7"/><rect x="56" y="30" width="7" height="7"/><rect x="52" y="46" width="7" height="7"/></svg>
    <h4>Digital Integration</h4><p>Includes digital portfolio of practice<br>(DPP) and skill bite certificates.</p>
  </div>
  <div class="feature" style="left:126px;top:600px">
    <svg viewBox="0 0 70 70" fill="none" stroke="#00A9DD" stroke-width="2.2"><rect x="4" y="8" width="62" height="42" rx="2"/><path d="M26 50v10M44 50v10M18 62h34"/><rect x="12" y="16" width="10" height="8"/><rect x="12" y="30" width="10" height="8"/><path d="M27 20h16M27 34h14"/><path d="M48 28l10 6-5 1 3 5-2 1-3-5-3 3z"/></svg>
    <h4>Practical Application</h4><p>Courses blend digital learning<br>with practical application.</p>
  </div>
  <div class="feature" style="left:453px;top:600px">
    <svg viewBox="0 0 70 70" fill="none" stroke="#00A9DD" stroke-width="2.2"><rect x="20" y="8" width="42" height="56" rx="3"/><rect x="32" y="4" width="18" height="8" rx="2"/><circle cx="22" cy="32" r="12"/><path d="M16 32l4 4 8-8"/><path d="M31 42l7 7"/><path d="M42 26h14M42 48h14M42 56h10"/></svg>
    <h4>Progress Monitoring</h4><p>Students are empowered in their<br>learning and development.</p>
  </div>
  <div class="feature" style="left:780px;top:600px">
    <svg viewBox="0 0 70 70" fill="none" stroke="#00A9DD" stroke-width="2.2"><path d="M34 8c-8-4-18 2-18 10-8 2-10 12-4 18-4 8 2 16 10 16 2 6 8 8 12 6z"/><path d="M34 8v50"/><path d="M34 20h14M34 32h20M34 44h14"/><circle cx="51" cy="20" r="3"/><circle cx="57" cy="32" r="3"/><circle cx="51" cy="44" r="3"/></svg>
    <h4>Customization</h4><p>AI-driven to tailor courses<br>to student needs.</p>
  </div>
</section>

<section class="invest">
  <h3>Invest in your Future Today!</h3>
  <p>We develop courses and make customized course provision that support academic achievement and social and emotional skills fostering personal growth and academic skill development that are relevant and timely for the learner. This prepares them for present and future challenges and opportunities, while contributing to students' career portfolio with an accredited, relevant and adaptive provision.</p>
  <a class="btn btn-solid" style="left:126px;top:285px;width:160px">Enroll Today <svg viewBox="0 0 14 14"><path d="M1 7h11M8 3l4 4-4 4" stroke="#fff" stroke-width="1.6" fill="none"/></svg></a>
  <a class="btn btn-ghost" style="left:309px;top:285px;width:160px">Our Courses <svg viewBox="0 0 14 14"><path d="M1 7h11M8 3l4 4-4 4" stroke="#fff" stroke-width="1.6" fill="none"/></svg></a>
  <div class="invest-photo" role="img" aria-label="Smiling young man in a denim jacket holding books"></div>
  <div class="invest-ring"></div>
  <svg class="abs" style="left:1085px;top:305px" width="26" height="26" viewBox="0 0 26 26" fill="none" stroke="#00A9DD" stroke-width="2"><path d="M3 3l20 20M23 3L3 23"/></svg>
</section>

<section class="testimonials">
  <div class="eyebrow" style="top:62px"><span>Testimonials</span></div>
  <h2 class="section-title" style="top:80px">What Our Students Are Saying</h2>
  <div class="quote-mark">“</div>
  <h4>A Journey of Personal Growth</h4>
  <p class="quote">The course provided me with essential life skills that have truly transformed my approach to work and personal life. From self-awareness to communication techniques, each module was insightful and practical. It laid a solid foundation for my journey through the subsequent levels.</p>
  <div class="t-arrow" style="left:126px"><svg width="16" height="16" viewBox="0 0 14 14"><path d="M13 7H2M6 3L2 7l4 4" stroke="#fff" stroke-width="1.6" fill="none"/></svg></div>
  <div class="t-arrow" style="left:1036px"><svg width="16" height="16" viewBox="0 0 14 14"><path d="M1 7h11M8 3l4 4-4 4" stroke="#fff" stroke-width="1.6" fill="none"/></svg></div>
  <div class="avatar" role="img" aria-label="Portrait of the student"></div>
  <div class="t-name">Mara Lindqvist</div>
  <div class="t-role">Level 1 Graduate</div>
  <div class="dots"><i></i><i class="on"></i><i></i><i></i><i></i></div>
</section>

<footer class="site-footer">
  <div class="logo abs" style="left:63px;top:146px">Logo Here</div>
  <div class="f-col abs" style="left:279px;top:146px">
    <h5>Main Links</h5>
    <ul class="f-links"><li>About Us</li><li>Our Courses</li><li>FAQs</li><li>Resources</li><li>Contact Us</li><li>Partnerships</li></ul>
  </div>
  <div class="f-col abs" style="left:484px;top:146px">
    <h5>Contact Info</h5>
    <ul class="f-contact">
      <li><svg viewBox="0 0 12 12"><path d="M6 11S2 7 2 4.5a4 4 0 018 0C10 7 6 11 6 11z" fill="#00BBA5"/><circle cx="6" cy="4.5" r="1.4" fill="#0c2f40"/></svg><span>123 Main Street, Suite 101,<br>Cityville, State, ZIP</span></li>
      <li><svg viewBox="0 0 12 12"><rect x="1" y="2.5" width="10" height="7" fill="#00BBA5"/><path d="M1 3l5 4 5-4" stroke="#0c2f40" fill="none"/></svg><span>info@lumenpathedu.example</span></li>
      <li><svg viewBox="0 0 12 12"><path d="M2 1.5l2.5-.5 1.3 3-1.5 1a6 6 0 003 3l1-1.5 3 1.3-.5 2.5C6 11 1 6 2 1.5z" fill="#00BBA5"/></svg><span>+1 (555) 010-2290</span></li>
      <li><svg viewBox="0 0 12 12"><circle cx="6" cy="6" r="5" fill="#00BBA5"/><path d="M6 3v3l2 1" stroke="#0c2f40" fill="none"/></svg><span>Monday – Friday<br>9am – 5pm</span></li>
    </ul>
  </div>
  <div class="f-col news abs" style="left:815px;top:146px">
    <h5>Subscribe to our Newsletter</h5>
    <p>Sign up to stay updated with the latest news, course offerings, and exclusive insights.</p>
    <div class="field"><svg width="12" height="10" viewBox="0 0 12 10"><rect x=".5" y=".5" width="11" height="9" fill="#8fa5b1"/><path d="M1 1l5 4 5-4" stroke="#0c2f40" fill="none"/></svg>Enter Email Address</div>
    <div class="sub">Subscribe <svg width="13" height="13" viewBox="0 0 14 14"><path d="M1 7h11M8 3l4 4-4 4" stroke="#fff" stroke-width="1.6" fill="none"/></svg></div>
  </div>
  <div class="f-bottom"></div>
  <div class="copyright">© 2024 Brand Name Here | All Rights Reserved</div>
  <div class="social" style="left:1080px;border-radius:50%"></div>
  <div class="social" style="left:1115px;border-radius:3px"></div>
</footer>

<div class="partners">
  <h3>Affiliated Partners</h3>
  <div class="badge" style="left:463px"><i></i></div>
  <div class="badge" style="left:608px"><i></i></div>
  <div class="badge" style="left:754px"><i></i></div>
  <div class="badge" style="left:900px"><i></i></div>
</div>

</body>
</html>
```